We need visit card and a letter paper for our website. thx

We have a beauty clinic in Switzerland.
https://wolkenbachtal.ch
We need a visit card.

Requirements
Must have
• see colors on website

```html
<!DOCTYPE html>
<html lang="de">
<head>
<meta charset="utf-8">
<title>Wolkenbachtal – Visitenkarte</title>
<link href="https://fonts.googleapis.com/css2?family=Montserrat:wght@300;400&display=swap" rel="stylesheet">
<style>
  :root {
    --backdrop: #d14f80;
    --card: #ffffff;
    --ink: #1c1c1c;
    --photo-tone: #f6e3ec;
  }
  html, body {
    margin: 0;
    width: 1200px;
    height: 1200px;
    overflow: hidden;
    background: var(--backdrop);
    font-family: "Montserrat", sans-serif;
    color: var(--ink);
  }
  .card {
    position: absolute;
    background: var(--card);
    overflow: hidden;
  }
  .card--front { left: 279px; top: 186px; width: 640px; height: 365px; }
  .card--back  { left: 290px; top: 650px; width: 618px; height: 354px; }

  .photo-area {
    position: absolute;
    background: var(--photo-tone);
  }

  .brand-name {
    position: absolute;
    margin: 0;
    font-weight: 400;
    white-space: nowrap;
    transform: translate(-50%, -50%);
    line-height: 1;
  }
  .card--front .brand-name { left: 320px; top: 168px; font-size: 34px; }
  .card--back  .brand-name { left: 133px; top: 176px; font-size: 22px; }

  .contact-frame { position: absolute; left: 0; top: 0; }

  .contact-line {
    position: absolute;
    left: 308px;
    margin: 0;
    font-weight: 300;
    font-size: 15px;
    line-height: 18px;
    white-space: nowrap;
  }
  .contact-line--name {
    font-weight: 400;
    font-size: 29px;
    line-height: 34px;
  }
</style>
</head>
<body>

<section class="card card--front" aria-label="Visitenkarte Vorderseite">
  <div class="photo-area" role="img" aria-label="Foto: Rosenblatt mit Wassertropfen" style="left:361px;top:10px;width:114px;height:102px;"></div>
  <div class="photo-area" role="img" aria-label="Foto: unscharfes Rosenblatt im Hintergrund" style="left:487px;top:62px;width:153px;height:280px;"></div>
  <p class="brand-name">Wolkenbachtal</p>
</section>

<section class="card card--back" aria-label="Visitenkarte Rückseite">
  <div class="photo-area" role="img" aria-label="Foto: unscharfes Rosenblatt im Hintergrund" style="left:0;top:30px;width:126px;height:272px;"></div>
  <div class="photo-area" role="img" aria-label="Foto: Rosenblatt mit Wassertropfen" style="left:160px;top:246px;width:109px;height:100px;"></div>
  <p class="brand-name">Wolkenbachtal</p>

  <svg class="contact-frame" width="618" height="354" viewBox="0 0 618 354" aria-hidden="true">
    <polyline points="372,71 372,55 618,55" fill="none" stroke="#1c1c1c" stroke-width="2.5"/>
    <polyline points="372,284 372,300 618,300" fill="none" stroke="#1c1c1c" stroke-width="2.5"/>
  </svg>

  <h1 class="contact-line contact-line--name" style="top:80px;">Dr. Lena Marti</h1>
  <p class="contact-line" style="top:119px;">DESA</p>
  <p class="contact-line" style="top:160px;">P: +41 (0) 800 24 60 60</p>
  <p class="contact-line" style="top:178px;">E: hallo@wolkenbachtal.ch</p>
  <p class="contact-line" style="top:215px;">Bergweg 14, 7188 Sedrun</p>
  <p class="contact-line" style="top:233px;">Switzerland</p>
  <p class="contact-line" style="top:266px;">www.wolkenbachtal.ch</p>
</section>

</body>
</html>
```